Small company security and risk consulting startup needs an explosive message via marketing colla...

Need a two page (front/back) flyer that calls out our three primary service areas incorporating brandmill developed logo and website visuals. Something that grabs attention at first glance to entice the viewer to read and connect for a services consultation. I will need the ability to make minor adjustments and add language.

```html
<!DOCTYPE html>
<html lang="en">
<head>
<meta charset="utf-8">
<title>Sentinel Ridge Consulting Services – Flyer</title>
<link rel="stylesheet" href="https://fonts.googleapis.com/css2?family=Open+Sans:wght@400;600;700&family=Teko:wght@600&family=Oswald:wght@500&display=swap">
<style>
  :root{
    --ink:#0d0d0f;
    --red:#b3171d;
    --red-bright:#d11f26;
    --white:#ffffff;
    --rule:#5a5a5e;
    --photo-dark:#2a3344;
    --photo-mid:#5d6d86;
    --photo-warm:#c9b8a6;
    --badge-blue:#2c4fa3;
  }
  *{box-sizing:border-box;margin:0;padding:0}
  html,body{width:1200px;height:793px;overflow:hidden;background:var(--white)}
  body{position:relative;font-family:"Open Sans",sans-serif;color:var(--white)}

  .page{position:absolute;top:36px;width:568px;height:730px;background:var(--ink);overflow:hidden}
  .page--front{left:25px}
  .page--back{left:607px}
  .shapes{position:absolute;inset:0;width:100%;height:100%}

  /* brand lockup */
  .brand{position:absolute;top:38px;width:250px;text-align:center}
  .brand__mark{display:block;width:26px;height:26px;border-radius:50%;background:var(--red);margin:0 auto 14px}
  .brand__name{font-weight:700;font-size:19px;letter-spacing:.5px;color:var(--red-bright);line-height:1}
  .brand__line{font-weight:600;font-size:7.5px;letter-spacing:4px;margin-top:4px}
  .brand__tag{font-size:5.5px;letter-spacing:2px;color:var(--red-bright);margin-top:2px}
  .page--front .brand{left:0}
  .page--back .brand{left:-6px}

  /* photos */
  .photo{position:absolute}
  .photo--team-walk{inset:0;clip-path:polygon(0 204px,568px 25px,568px 310px,0 508px);
    background:linear-gradient(120deg,var(--photo-dark),var(--photo-mid) 45%,#1c2230)}
  .photo--circle{border-radius:50%;border:3px solid var(--red);
    background:radial-gradient(circle at 40% 40%,var(--photo-warm),#8a7a6c 70%,#4a4a50)}
  .photo--circle.cool{background:radial-gradient(circle at 60% 40%,#e2e6ea,#7b8590 60%,#2e3238)}

  .headline{position:absolute;font-family:"Teko",sans-serif;font-weight:600;line-height:1;text-align:center;
    text-shadow:2px 2px 0 var(--red)}
  .front-title{left:0;width:568px;top:500px;font-size:62px;letter-spacing:2px}
  .front-strap{position:absolute;left:113px;top:548px;width:337px;height:28px;background:var(--red);
    border-radius:3px;font-weight:700;font-size:14.5px;letter-spacing:1px;text-align:center;line-height:28px}
  .front-copy{position:absolute;left:30px;width:508px;top:582px;font-size:9.6px;line-height:12.6px;
    text-align:center;letter-spacing:.4px}
  .front-cta{position:absolute;left:182px;width:214px;top:626px;height:28px;border-top:1.5px solid var(--red);
    border-bottom:1.5px solid var(--red);font-family:"Oswald",sans-serif;font-weight:500;font-size:16px;
    text-align:center;line-height:25px;letter-spacing:.5px}

  .contact{position:absolute;display:flex;align-items:center;gap:8px;font-weight:700;color:var(--white);white-space:nowrap}
  .contact svg{flex:none}
  .front-contact{font-style:italic;font-size:18px;letter-spacing:1px;top:684px}
  .front-contact--phone{left:36px}
  .front-contact--mail{left:326px}

  /* back */
  .back-title{left:0;width:568px;top:203px;font-size:57px;letter-spacing:3px}
  .back-sub{position:absolute;left:0;width:568px;top:247px;text-align:center;font-weight:700;font-size:18.5px;letter-spacing:1.5px}
  .back-intro{position:absolute;left:28px;width:512px;top:278px;font-size:9.6px;line-height:12.6px;
    text-align:center;letter-spacing:.4px}
  .service{position:absolute;left:26px;width:520px;display:flex;gap:16px}
  .service__icon{flex:none;width:60px;height:52px}
  .service__body{width:425px}
  .service__title{font-weight:700;font-size:16.5px;letter-spacing:1px;line-height:1.1}
  .service__text{font-size:8.4px;line-height:11px;margin-top:4px}
  .service--security{top:340px}
  .service--risk{top:432px}
  .service--consulting{top:512px}
  .divider{position:absolute;left:102px;width:401px;height:1px;background:var(--rule)}
  .perks{position:absolute;left:26px;top:601px;list-style:none;font-size:10px;letter-spacing:.9px;line-height:18px}
  .perks li::before{content:"";display:inline-block;width:4px;height:4px;border-radius:50%;background:var(--white);
    margin-right:5px;vertical-align:middle}
  .badge{position:absolute;left:452px;top:620px;width:90px;height:89px;background:var(--white);display:flex;
    align-items:center;justify-content:center;z-index:2}
  .badge span{width:74px;height:74px;border-radius:50%;border:4px solid var(--badge-blue)}
  .back-footer-rule{position:absolute;left:0;top:676px;width:568px;height:2px;background:var(--white)}
  .back-contact{font-size:18.5px;top:691px;font-weight:600}
  .back-contact--phone{left:24px}
  .back-contact--mail{left:235px}
</style>
</head>
<body>

<section class="page page--front">
  <svg class="shapes" viewBox="0 0 568 730" aria-hidden="true">
    <polygon points="200,143 568,0 568,30" fill="var(--red)"/>
    <polygon points="0,508 360,384 0,546" fill="var(--red)"/>
    <polygon points="0,670 234,670 272,730 0,730" fill="var(--red)"/>
    <polygon points="328,670 568,670 568,730 272,730" fill="var(--red)"/>
  </svg>
  <div class="photo photo--team-walk" role="img" aria-label="Two consultants walking through a server room"></div>
  <div class="photo photo--circle" style="left:358px;top:278px;width:164px;height:164px" role="img" aria-label="Two colleagues reviewing work on a laptop"></div>
  <div class="photo photo--circle cool" style="left:315px;top:350px;width:122px;height:122px" role="img" aria-label="Team collaborating at computer desks"></div>

  <div class="brand">
    <span class="brand__mark"></span>
    <div class="brand__name">Sentinel Ridge</div>
    <div class="brand__line">CONSULTING SERVICES</div>
    <div class="brand__tag">commitment - integrity - results</div>
  </div>

  <h1 class="headline front-title">LOREM IPSUM</h1>
  <div class="front-strap">EXCEPTEUR SINT OCCAECAT CUPIDATAT</div>
  <p class="front-copy">consectetur adipiscing elit, sed do eiusmod tempor incididunt ut labore et dolore magna aliqua. Ut enim ad minim veniam, quis nostrud exercitation ullamco laboris nisi ut aliquip ex ea commodo consequat. Duis aute irure dolor in reprehenderit</p>
  <div class="front-cta">CONSECTETUR ADIPISCING ELIT</div>

  <div class="contact front-contact front-contact--phone">
    <svg width="20" height="20" viewBox="0 0 20 20"><rect width="20" height="20" rx="4" fill="var(--white)"/><path d="M7 4c1 0 1.5 2.5 1 3.5l-1 .8c.6 1.8 1.8 3.2 3.6 4l.9-1c1-.4 3.3.3 3.3 1.3 0 1.6-1.4 2.6-3 2.2C8 14 5.6 11 4.8 7.6 4.4 5.6 5.5 4 7 4z" fill="var(--red)"/></svg>
    call us 555019247
  </div>
  <div class="contact front-contact front-contact--mail">
    <svg width="24" height="17" viewBox="0 0 24 17"><rect x="1" y="1" width="22" height="15" fill="none" stroke="var(--white)" stroke-width="1.6"/><path d="M1 1l11 9 11-9M1 16l8-7M23 16l-8-7" fill="none" stroke="var(--white)" stroke-width="1.6"/></svg>
    info@sridge.com
  </div>
</section>

<section class="page page--back">
  <svg class="shapes" viewBox="0 0 568 730" aria-hidden="true">
    <polygon points="0,176 568,51 568,95 0,181" fill="var(--red)"/>
    <rect x="0" y="678" width="568" height="52" fill="var(--red)"/>
  </svg>
  <div class="photo photo--circle cool" style="left:367px;top:23px;width:154px;height:154px" role="img" aria-label="Hands typing code on a laptop keyboard"></div>
  <div class="photo photo--circle" style="left:283px;top:51px;width:124px;height:124px" role="img" aria-label="Team collaborating at computer desks"></div>

  <div class="brand">
    <span class="brand__mark"></span>
    <div class="brand__name">Sentinel Ridge</div>
    <div class="brand__line">CONSULTING SERVICES</div>
    <div class="brand__tag">commitment - integrity - results</div>
  </div>

  <h2 class="headline back-title">LOREM IPSUM DOLOR</h2>
  <div class="back-sub">SED DO EIUSMOD TEMPOR INCIDIDUNT</div>
  <p class="back-intro">Lorem ipsum dolor sit amet, consectetur adipiscing elit, sed do eiusmod tempor incididunt ut labore et dolore magna aliqua. Ut enim ad minim veniam, quis nostrud exercitation ullamco laboris nisi ut aliquip ex ea commodo consequat. Duis aute irure dolor in reprehenderit in voluptate velit esse cillum dolore eu fugiat nulla pariatur. Excepteur</p>

  <div class="service service--security">
    <svg class="service__icon" viewBox="0 0 60 52" fill="none" stroke="var(--white)" stroke-width="2.2"><rect x="4" y="2" width="52" height="38" rx="2"/><rect x="8" y="6" width="44" height="30"/><path d="M1 44h58v3H1z"/><path d="M14 21c8-9 24-9 32 0-8 9-24 9-32 0z"/><circle cx="30" cy="21" r="4.5"/></svg>
    <div class="service__body">
      <div class="service__title">SECURITY PROGRAMS</div>
      <p class="service__text">Lorem ipsum dolor sit amet, consectetur adipiscing elit, sed do eiusmod tempor incididunt ut labore et dolore magna aliqua. Ut enim ad minim veniam, quis nostrud exercitation ullamco laboris nisi ut aliquip ex ea commodo consequat. Duis aute irure dolor in reprehenderit</p>
    </div>
  </div>
  <div class="divider" style="top:414px"></div>

  <div class="service service--risk">
    <svg class="service__icon" viewBox="0 0 60 60" style="height:60px"><path d="M24 58V46c-6-3-10-9-10-16 0-11 8-19 19-19s18 7 18 16l5 9-5 2v6c0 3-2 4-5 4h-5v10z" fill="var(--white)"/><circle cx="17" cy="17" r="10" fill="var(--ink)" stroke="var(--white)" stroke-width="5" stroke-dasharray="4 3"/><circle cx="17" cy="17" r="4" fill="var(--white)"/></svg>
    <div class="service__body">
      <div class="service__title">RISK MANAGEMENT SERVICES</div>
      <p class="service__text">Lorem ipsum dolor sit amet, consectetur adipiscing elit, sed do eiusmod tempor incididunt ut labore et dolore magna aliqua. Ut enim ad minim veniam, quis nostrud exercitation ullamco</p>
    </div>
  </div>
  <div class="divider" style="top:500px"></div>

  <div class="service service--consulting">
    <svg class="service__icon" viewBox="0 0 60 56" style="height:56px"><g fill="var(--white)"><circle cx="42" cy="6" r="5"/><path d="M32 26l4-12h12l4 12z"/><circle cx="14" cy="32" r="5"/><path d="M4 54l4-14h12l4 14z"/></g><g fill="none" stroke="var(--white)" stroke-width="2"><path d="M26 6C16 6 10 12 9 20"/><path d="M34 50c10 0 16-6 17-14"/></g><g fill="var(--white)"><path d="M5 18l4 5 4-5z"/><path d="M47 38l4-5 4 5z"/></g></svg>
    <div class="service__body">
      <div class="service__title">CONSULTING SERVICES</div>
      <p class="service__text">Lorem ipsum dolor sit amet, consectetur adipiscing elit, sed do eiusmod tempor incididunt ut labore et dolore magna aliqua. Ut enim ad minim veniam, quis nostrud exercitation ullamco laboris nisi ut aliquip ex ea commodo consequat.</p>
    </div>
  </div>

  <ul class="perks">
    <li>Duis aute irure dolor in reprehenderit in voluptate velit esse</li>
    <li>Cillum dolore eu fugiat nulla pariatur. Excepteur sint occaecat</li>
    <li>Cupidatat non proident, sunt in culpa qui officia deserunt</li>
    <li>Mollit anim id est laborum.</li>
  </ul>

  <div class="badge" role="img" aria-label="Certification badge"><span></span></div>

  <div class="back-footer-rule"></div>
  <div class="contact back-contact back-contact--phone">
    <svg width="20" height="20" viewBox="0 0 20 20"><rect width="20" height="20" rx="4" fill="var(--white)"/><path d="M7 4c1 0 1.5 2.5 1 3.5l-1 .8c.6 1.8 1.8 3.2 3.6 4l.9-1c1-.4 3.3.3 3.3 1.3 0 1.6-1.4 2.6-3 2.2C8 14 5.6 11 4.8 7.6 4.4 5.6 5.5 4 7 4z" fill="var(--red)"/></svg>
    call us 555019247
  </div>
  <div class="contact back-contact back-contact--mail">
    <svg width="22" height="16" viewBox="0 0 24 17"><rect x="1" y="1" width="22" height="15" fill="none" stroke="var(--white)" stroke-width="1.6"/><path d="M1 1l11 9 11-9M1 16l8-7M23 16l-8-7" fill="none" stroke="var(--white)" stroke-width="1.6"/></svg>
    info@sridge.com
  </div>
</section>

</body>
</html>
```